DELMORAN Auto Battery

We need top of the line design for a new product that we are launching, Automotive Batteries.
We are an exporter of Auto Spare parts based in China, our new products will be launched in October 2012, the website is to be presented as B2B not B2C, we deal directly with Importers all around the world.
Our vision for the website is to be Clean, elegant, smart, warm, reflects confidence and trust..therefore, the choice of themes, colors, fonts and graphics should take into considerations all above.
Since there are hundreds of Battery types, specs, sizes, weight...etc, we will need a upload template that will enable us to upload, modify and manipulate the data of the batteries.
Car battery importers
Automotive

```html
<!DOCTYPE html>
<html lang="en">
<head>
<meta charset="utf-8">
<title>DELMORAN Auto Battery</title>
<link rel="stylesheet" href="https://fonts.googleapis.com/css2?family=Open+Sans:wght@400;600;700&family=Noto+Sans:wght@400;700&display=swap">
<style>
:root{
  --ink-dark:#0b0b0b;
  --bar:#121212;
  --bar-edge:#3a3a3a;
  --white:#ffffff;
  --text-light:#e6e6e6;
  --text-body:#4a4a4a;
  --text-heading:#3c3c3c;
  --accent:#1a78d0;
  --btn:#0f4c8a;
  --btn-top:#1c5fa3;
  --field-border:#c8c8c8;
  --page-light:#e9e9e9;
}
*{margin:0;padding:0;box-sizing:border-box}
html,body{width:982px;height:1200px;overflow:hidden}
body{font-family:"Open Sans",sans-serif;background:var(--page-light)}
.canvas{position:relative;width:982px;height:1200px;overflow:hidden;
  background:linear-gradient(180deg,#2a2a2a 0,#3a3a3a 180px,#4c4c4c 420px,#bdbdbd 560px,#ececec 620px,#e4e4e4 900px,#d2d2d2 1100px,#c4c4c4 1200px)}
.canvas::before{content:"";position:absolute;left:0;top:0;width:982px;height:600px;
  background:radial-gradient(ellipse 420px 260px at 680px 400px,rgba(255,255,255,.25),transparent 70%),
             radial-gradient(ellipse 600px 300px at 200px 60px,rgba(255,255,255,.08),transparent 70%)}
.abs{position:absolute}

.brand{left:109px;top:54px;color:var(--white)}
.brand-name{font-size:38px;font-weight:600;letter-spacing:.5px;line-height:1}
.brand-tag{font-size:22px;margin-left:24px;line-height:1.2}

.call{left:478px;top:84px;color:var(--text-light);font-size:16px}
.search{left:729px;top:83px;width:156px;height:26px;background:linear-gradient(#fff,#e6e6e6);border-radius:2px;
  font-size:13px;color:#333;padding:4px 8px}
.search svg{position:absolute;right:6px;top:5px}

.nav{left:56px;top:143px;width:866px;height:50px;border-radius:6px;
  background:linear-gradient(#2a2a2a,#050505);border:1px solid var(--bar-edge);box-shadow:0 6px 12px rgba(0,0,0,.6)}
.nav-link{position:absolute;top:15px;color:var(--white);font-size:14px;font-weight:600}
.nav-link.is-active{color:var(--accent)}
.slider-dots{position:absolute;left:748px;top:8px;width:85px;height:32px;border-radius:5px;background:#000;border:1px solid #333;
  display:flex;gap:6px;align-items:center;justify-content:center}
.dot{width:14px;height:14px;border-radius:50%;background:#bbb}
.dot.is-current{background:var(--btn-top);border:2px solid #ccc}
.slider-label{left:782px;top:191px;width:130px;height:28px;border-radius:0 0 6px 6px;background:#111;color:#ccc;font-size:12.5px;text-align:center;line-height:24px}

.hero-title{left:105px;top:284px;color:var(--text-light);font-size:21px;font-weight:700;letter-spacing:.4px}
.hero-text{left:105px;top:321px;width:350px;color:var(--text-light);font-family:"Noto Sans",sans-serif;font-size:17px;line-height:22px;text-align:justify;letter-spacing:.6px}
.hero-product{left:560px;top:262px;width:300px;height:262px;
  background:radial-gradient(ellipse 150px 130px at 50% 50%,rgba(225,228,235,.75),rgba(180,185,195,.35) 60%,transparent 100%)}

.section-title{font-size:20px;font-weight:400;color:var(--text-heading)}
.section-title b{font-weight:400;color:var(--accent)}
.divider{left:106px;top:630px;width:766px;height:2px;background:linear-gradient(90deg,transparent,#c6c6c6 20%,#c6c6c6 80%,transparent)}
.welcome-text{left:106px;top:651px;width:504px;font-family:"Noto Sans",sans-serif;font-size:15.5px;line-height:24px;letter-spacing:.25px;color:var(--text-body);text-align:justify}
.btn{position:absolute;height:26px;border-radius:3px;background:linear-gradient(var(--btn-top),var(--btn));color:var(--white);font-size:13.5px;text-align:center;line-height:26px}
.field{position:absolute;left:642px;width:230px;height:29px;background:#fff;border:1px solid var(--field-border);font-size:13.5px;color:#555;padding:5px 7px}
.small-label{font-size:13.5px;color:#444}

.catalogue{left:106px;top:840px;width:770px;height:208px;border-radius:5px;background:linear-gradient(#3c3c3c,#161616 40px,#232323);border:2px solid #000;box-shadow:0 4px 8px rgba(0,0,0,.5)}
.catalogue-title{position:absolute;left:28px;top:12px;color:var(--white);font-size:16px}
.catalogue-arrows{position:absolute;right:30px;top:12px}
.catalogue-rule{position:absolute;left:0;top:42px;width:100%;height:1px;background:#444}
.thumb{position:absolute;top:60px;width:163px;height:109px;border:1px solid #555;background:linear-gradient(135deg,#8a9ab8,#e8e8e8 60%,#6a6a6a)}
.thumb-caption{position:absolute;top:180px;color:var(--white);font-size:13.5px}

.footer{left:47px;top:1083px;width:894px;height:66px;border-radius:4px;background:linear-gradient(#222,#0a0a0a);border:2px solid #000;box-shadow:0 18px 20px -8px rgba(0,0,0,.45)}
.copyright{position:absolute;left:24px;top:26px;color:#ddd;font-size:11px}
.foot-link{position:absolute;top:26px;color:var(--white);font-size:11.5px;font-weight:600}
.foot-link.is-active{color:var(--accent)}
</style>
</head>
<body>
<div class="canvas">
  <header>
    <div class="abs brand"><div class="brand-name">DELMORAN</div><div class="brand-tag">Auto Battery</div></div>
    <div class="abs call">Call Us :&nbsp; +86 (20) 5550 1274</div>
    <div class="abs search">search here
      <svg width="16" height="16" viewBox="0 0 16 16"><circle cx="9.5" cy="6.5" r="4.5" fill="none" stroke="#333" stroke-width="1.6"/><line x1="6.3" y1="9.7" x2="2" y2="14" stroke="#333" stroke-width="2"/></svg>
    </div>
    <nav class="abs nav">
      <span class="nav-link is-active" style="left:61px">Home</span>
      <span class="nav-link" style="left:154px">About Us</span>
      <span class="nav-link" style="left:269px">Products</span>
      <span class="nav-link" style="left:382px">Services</span>
      <span class="nav-link" style="left:493px">Our Clients</span>
      <span class="nav-link" style="left:623px">Contact Us</span>
      <div class="slider-dots"><span class="dot is-current"></span><span class="dot"></span><span class="dot"></span></div>
    </nav>
    <div class="abs slider-label">slider controls</div>
  </header>

  <section>
    <h2 class="abs hero-title">Put some text here</h2>
    <p class="abs hero-text">Since there are hundreds of Battery types, specs, sizes, weight...etc, we will need a upload template that will enable us to upload, modify and manipulate the data of the batteries.</p>
    <div class="abs hero-product" role="img" aria-label="Product photo of a car battery"></div>
  </section>

  <section>
    <h2 class="abs section-title" style="left:107px;top:589px"><b>Welcome</b> to our site</h2>
    <h2 class="abs section-title" style="left:643px;top:589px"><b>Login</b> for feedback</h2>
    <div class="abs divider"></div>
    <p class="abs welcome-text">We need top of the line design for a new product that we are launching, Automotive Batteries.We are an exporter of Auto Spare parts based in China, our new products will be launched in October 2012, the website is to be presented as B2B not B2C, we deal directly with Importers all around the world.</p>
    <span class="btn" style="left:535px;top:775px;width:74px">More</span>

    <div class="field" style="top:655px">User id</div>
    <div class="field" style="top:690px">Password</div>
    <span class="abs small-label" style="left:647px;top:734px">Forget Password ?</span>
    <span class="btn" style="left:799px;top:729px;width:74px">Login</span>
    <span class="abs small-label" style="left:649px;top:777px">New User ?</span>
    <span class="btn" style="left:753px;top:774px;width:120px">Register here</span>
  </section>

  <section class="abs catalogue">
    <span class="catalogue-title">Products Catalogue</span>
    <svg class="catalogue-arrows" width="34" height="20" viewBox="0 0 34 20"><polyline points="12,3 4,10 12,17" fill="none" stroke="#aaa" stroke-width="2.5"/><polyline points="22,3 30,10 22,17" fill="none" stroke="#aaa" stroke-width="2.5"/></svg>
    <div class="catalogue-rule"></div>
    <div class="thumb" style="left:29px" role="img" aria-label="Product photo of batteries"></div>
    <div class="thumb" style="left:211px" role="img" aria-label="Product photo of a battery"></div>
    <div class="thumb" style="left:394px" role="img" aria-label="Product photo of batteries"></div>
    <div class="thumb" style="left:577px" role="img" aria-label="Product photo of a battery"></div>
    <span class="thumb-caption" style="left:30px">Product Model No.</span>
    <span class="thumb-caption" style="left:212px">Product Model No.</span>
    <span class="thumb-caption" style="left:396px">Product Model No.</span>
    <span class="thumb-caption" style="left:577px">Product Model No.</span>
  </section>

  <footer class="abs footer">
    <span class="copyright">copyright © 2010&nbsp; DELMORAN</span>
    <span class="foot-link is-active" style="left:323px">Home</span>
    <span class="foot-link" style="left:400px">About Us</span>
    <span class="foot-link" style="left:495px">Products</span>
    <span class="foot-link" style="left:589px">Services</span>
    <span class="foot-link" style="left:679px">Our Clients</span>
    <span class="foot-link" style="left:787px">Contact Us</span>
  </footer>
</div>
</body>
</html>
```